Shopify Design for wedding invitations

We are a greeting card manufactory, special in wedding invitation
I need a shopify website for our wedding invitation brand. (Lovmira), atttach you can find our logo.
We are looking for someone to create a modern and clean looking e-commerce store for our wedding invitation through Shopify. We need some life, professionalism and style put into our site. We will have a variety serie of products : laser cut wedding invitation, popup wedding invitaiton, vintage wedding invitation, handmade wedding invitation, printing invitation, Custom wedding cards, wedding stationery (including favor box, table card, place card, escort card, number card), Thank you card. our online store requires easy navigation to categories divided by product type.

our market is , Eourpe and USA,
please choose a good color for it.
you can go to our website: www.bluestonecraft.com and check our product.
also you can go to Vendoro 4 new items.
https://www.vendoro-shop.com/dp/X47K8Q2M19?ref=abc_item_dp

Target Market(s)

Europe and USA

Industry/Entity Type

wedding

Number of Pages Required

1 page

Requirements
Must have
• Logo, 3 banners than can be changed each 3-5 seconds.
Nice to have
• nice icon and font, beautiful color,

```html
<!DOCTYPE html>
<html lang="en">
<head>
<meta charset="utf-8">
<title>Lovmira — Wedding Invitations</title>
<link rel="stylesheet" href="https://fonts.googleapis.com/css2?family=Playfair+Display:wght@400;500&family=Nunito+Sans:wght@400;600;700&display=swap">
<style>
:root{
  --maroon:#5e1718;
  --maroon-text:#6b2a28;
  --tan:#c7a592;
  --box:#e9eaea;
  --ink:#222;
  --serif:'Playfair Display',Georgia,serif;
  --sans:'Nunito Sans',Arial,sans-serif;
}
*{box-sizing:border-box;margin:0;padding:0}
html,body{width:1200px;height:3520px;overflow:hidden;background:#fff;font-family:var(--sans);color:var(--ink)}
.page{position:relative;width:1200px;height:3520px;overflow:hidden}
.abs{position:absolute}

.site-header{position:absolute;top:0;left:0;width:1200px;height:57px;background:#fff;z-index:2}
.brand{position:absolute;left:66px;top:10px;font-family:var(--serif);font-size:30px;color:var(--maroon-text)}
.main-nav{position:absolute;left:340px;top:18px;display:flex}
.main-nav a{font-family:var(--serif);font-size:17px;color:#8a8a8a;text-decoration:none;width:138px}

.hero{position:absolute;top:57px;left:0;width:1200px;height:510px;background:linear-gradient(90deg,#efefef 0%,#ebebea 50%,#e2dedb 100%)}
.hero-photo{position:absolute;right:0;top:0;width:560px;height:510px;background:radial-gradient(ellipse at 55% 45%,#f4f0ec 0%,#ddd5cc 55%,#cfc6bc 100%)}
.hero h1{position:absolute;left:172px;top:44px;font-family:var(--serif);font-weight:400;line-height:1}
.hero .happy{display:block;font-size:92px;color:#111}
.hero .wedding{display:block;font-size:152px;color:var(--maroon);margin-top:-6px;letter-spacing:-1px}
.hero p{position:absolute;left:186px;top:276px;font-size:27px;line-height:47px;color:#111}
.btn-shop{position:absolute;left:186px;top:388px;width:356px;height:46px;background:var(--maroon);color:#fff;border-radius:6px;font-size:21px;font-weight:600;display:flex;align-items:center;justify-content:center}
.slider-nav{position:absolute;left:40px;top:135px;width:20px}
.slider-nav .dot{display:block;width:13px;height:13px;border:1px solid #fff;border-radius:50%;margin:0 auto 14px}
.slider-nav .dot.active{background:var(--maroon);border-color:var(--maroon)}

.feature{position:absolute;top:613px;width:291px;height:98px;background:var(--box);border-radius:4px;display:flex;align-items:center;padding-left:44px;gap:16px}
.feature strong{display:block;font-size:15px;font-weight:700;color:#111}
.feature span{display:block;font-size:11px;color:#333;margin-top:6px}

.section-title{position:absolute;left:0;width:1200px;text-align:center;font-family:var(--serif);font-weight:400;color:var(--maroon-text)}

.categories{position:absolute;left:68px;top:833px;width:1078px;height:696px;display:grid;grid-template-columns:repeat(3,1fr);grid-template-rows:repeat(4,1fr)}
.tile{position:relative;display:flex;align-items:center;padding-left:66px;font-family:var(--serif);font-size:31px;line-height:40px}
.tile::before{content:"";position:absolute;left:55px;top:38px;bottom:0;border-left:2px solid rgba(255,255,255,.55)}
.tile.dark{background:var(--maroon);color:#e5cfc3}
.tile.light{background:var(--tan);color:var(--maroon-text)}
.tile.light::before{border-color:var(--maroon)}
.c1{grid-column:1}.c2{grid-column:2}.c3{grid-column:3}
.r1{grid-row:1}.r2{grid-row:2}.r3{grid-row:3}.r4{grid-row:4}.r23{grid-row:2/4}
.ph-rings{background:linear-gradient(135deg,#f3d9de,#d9c4c9 50%,#e7e1e4)}
.ph-paper{background:radial-gradient(circle at 50% 55%,#ece4d4 0 15%,#d9d8d4 30%,#bfc1b9 70%,#9a8f76)}
.ph-menu{background:linear-gradient(160deg,#cfd8d0,#eae6e3 45%,#d9d3cd)}
.ph-hands{background:linear-gradient(120deg,#c9d3d6,#e6ece9 55%,#c59d86)}

.tabs{position:absolute;top:1697px;left:0;width:1200px;display:flex;justify-content:center;gap:30px;font-size:13px;color:#222}
.tabs .on{color:var(--maroon-text)}
.product{position:absolute;top:1736px;width:248px;height:248px;background:linear-gradient(135deg,#7a3f22,#a0582c 55%,#6e361c)}
.product i{position:absolute;left:40px;top:50px;width:168px;height:150px;border-radius:2px}
.carousel-arrow{position:absolute;top:1850px}
.btn-view{position:absolute;left:493px;top:2021px;width:195px;height:46px;border:1.5px solid var(--maroon-text);border-radius:4px;color:var(--maroon-text);font-size:14px;font-weight:700;display:flex;align-items:center;justify-content:center;gap:8px}

.testimonials{position:absolute;top:2116px;left:0;width:1200px;height:490px;background:#f5f5f5;overflow:hidden}
.review{position:absolute;top:129px;width:516px;height:252px;background:#fff;border-radius:4px;text-align:center;padding-top:26px}
.stars{color:#e9b93c;font-size:15px;letter-spacing:1px}
.review p{font-size:11px;line-height:23px;color:#333;margin-top:14px;white-space:nowrap}
.avatar{width:48px;height:48px;border-radius:50%;background:#5b5450;margin:10px auto 0;position:relative}
.avatar::after{content:"";position:absolute;right:-3px;bottom:-2px;width:15px;height:15px;border-radius:50%;background:#3b8be0;border:2px solid #fff}
.review b{display:block;font-size:11px;margin-top:10px;color:#111}
.pager{position:absolute;top:425px;left:583px;display:flex;gap:8px}
.pager i{width:6px;height:6px;border-radius:50%;background:#b8d6d4}
.pager i:first-child{background:#2a8c86}

.newsletter{position:absolute;top:2604px;left:0;width:1200px;height:202px;background:var(--maroon);text-align:center;color:#e8cfc5}
.newsletter small{display:block;font-size:12px;margin-top:34px}
.newsletter h2{font-family:var(--serif);font-weight:400;font-size:29px;margin-top:6px;color:#f1dfd7}
.signup{position:absolute;left:417px;top:112px;width:361px;height:33px;border:1.5px solid var(--tan);display:flex;align-items:center}
.signup span{flex:1;text-align:left;font-size:12px;padding-left:14px;display:flex;align-items:center;gap:14px;color:#e0c6bb}
.signup b{width:86px;height:100%;background:var(--tan);color:var(--maroon);font-weight:400;font-size:12px;display:flex;align-items:center;justify-content:center}

.social{position:absolute;top:2806px;height:250px}
.follow{background:var(--tan);color:#fff;font-family:var(--serif);font-size:29px;line-height:40px;text-align:center;display:flex;align-items:center;justify-content:center;box-shadow:0 6px 12px rgba(0,0,0,.12)}

.foot-col{position:absolute;top:3120px;font-size:12px;line-height:25px;color:#222}
.foot-col.caps{text-transform:uppercase}
.foot-social small{font-size:12px;display:block}
.foot-social strong{font-size:25px;font-weight:400;display:block;line-height:28px}
.foot-social .icons{display:flex;gap:14px;margin-top:14px}
.foot-social .icons i{width:16px;height:16px;border-radius:50%;background:var(--maroon)}
.divider{position:absolute;top:3329px;left:56px;width:1074px;border-top:1px solid #ccc}
.foot-logo{position:absolute;left:520px;top:3256px;width:146px;height:146px;border-radius:50%;background:var(--tan);display:flex;align-items:center;justify-content:center;font-family:var(--serif);font-size:28px;color:var(--maroon-text)}
.copyright{position:absolute;top:3433px;left:0;width:1200px;text-align:center;font-size:11px;color:#999}
</style>
</head>
<body>
<div class="page">

<header class="site-header">
  <div class="brand">Lovmira</div>
  <nav class="main-nav">
    <a>Home</a><a>Products</a><a>News</a><a>About us</a><a>Contact us</a><a>Send inquery</a>
  </nav>
</header>

<section class="hero">
  <div class="hero-photo" role="img" aria-label="Bride in a white gown seated on a cream armchair holding a sprig of flowers"></div>
  <h1><span class="happy">Happy</span><span class="wedding">Wedding</span></h1>
  <p>Pass you’s happiness and joy in the<br>important days of your life</p>
  <div class="btn-shop">SHOP NOW</div>
  <div class="slider-nav">
    <svg width="20" height="22" viewBox="0 0 20 22" style="display:block;margin-bottom:26px"><path d="M10 20V3M4 9l6-6 6 6" stroke="#fff" stroke-width="1.5" fill="none"/></svg>
    <i class="dot"></i><i class="dot"></i><i class="dot"></i><i class="dot active"></i><i class="dot"></i>
    <svg width="20" height="22" viewBox="0 0 20 22" style="display:block;margin-top:12px"><path d="M10 2v17M4 13l6 6 6-6" stroke="#fff" stroke-width="1.5" fill="none"/></svg>
  </div>
</section>

<div class="feature" style="left:128px">
  <svg width="28" height="30" viewBox="0 0 28 30"><path d="M14 2l10 4v8c0 7-5 11-10 13C9 25 4 21 4 14V6z" fill="none" stroke="#222" stroke-width="1.8"/><path d="M9 15l4 4 6-7" fill="none" stroke="#222" stroke-width="1.8"/></svg>
  <div><strong>100% PERFECT</strong><span>30-Day Happiness Guarantee</span></div>
</div>
<div class="feature" style="left:453px">
  <svg width="30" height="24" viewBox="0 0 30 24"><path d="M2 4h16v13H2zM18 9h6l4 5v3h-10" fill="none" stroke="#222" stroke-width="1.8"/><circle cx="8" cy="19" r="2.5" fill="#e9eaea" stroke="#222" stroke-width="1.8"/><circle cx="23" cy="19" r="2.5" fill="#e9eaea" stroke="#222" stroke-width="1.8"/></svg>
  <div><strong>FREE SHIPPING.</strong><span>ParcelWay Express FREE SHIPPING.</span></div>
</div>
<div class="feature" style="left:777px">
  <svg width="30" height="30" viewBox="0 0 30 30"><path d="M15 3l11 5v13l-11 6-11-6V8zM4 8l11 5 11-5M15 13v14M9 5.5l11 5" fill="none" stroke="#222" stroke-width="1.8"/></svg>
  <div><strong>SMALL BATCHES</strong><span>We Ship everyday</span></div>
</div>

<h2 class="section-title" style="top:768px;font-size:31px">Shop by Categories</h2>

<section class="categories">
  <div class="tile dark c1 r1">Wedding invitation<br>card</div>
  <div class="ph-rings c2 r1" role="img" aria-label="Wedding rings resting on pink roses and baby's breath"></div>
  <div class="tile dark c3 r1">Wedding stationary</div>
  <div class="ph-paper c1 r23" role="img" aria-label="Blank handmade paper card among dried flowers on stone"></div>
  <div class="tile light c2 r2">Wedding decoration<br>accessory</div>
  <div class="ph-menu c3 r23" role="img" aria-label="Wreath-printed wedding menu cards on a set table"></div>
  <div class="tile dark c2 r3">Greeting card</div>
  <div class="tile light c1 r4">Laser cut favor box</div>
  <div class="ph-hands c2 r4" role="img" aria-label="Couple's hands with wedding rings and lavender"></div>
  <div class="tile light c3 r4">3D pop up card</div>
</section>

<h2 class="section-title" style="top:1634px;font-size:31px">Explore Items</h2>
<div class="tabs"><span class="on">POPULAR</span><span>NEW ARRIVALS</span><span>BEST SELLERS</span><span>SPECIAL OCCASIONS</span></div>

<svg class="carousel-arrow" style="left:38px" width="14" height="24" viewBox="0 0 14 24"><path d="M12 2L2 12l10 10" fill="none" stroke="#999" stroke-width="1.5"/></svg>
<div class="product" style="left:75px" role="img" aria-label="Gold lace laser cut invitation with kraft envelope on wood"><i style="background:linear-gradient(135deg,#c9a35a,#e8e0d0)"></i></div>
<div class="product" style="left:341px" role="img" aria-label="Ivory laser cut invitation with white envelope on wood"><i style="background:linear-gradient(135deg,#f5f3ef,#e7dcc5)"></i></div>
<div class="product" style="left:607px" role="img" aria-label="Gold butterfly laser cut invitation with kraft envelope on wood"><i style="background:linear-gradient(135deg,#d6ad73,#c49a5d)"></i></div>
<div class="product" style="left:873px" role="img" aria-label="Burgundy laser cut invitation with ribbon and kraft envelope on wood"><i style="background:linear-gradient(135deg,#d8b487,#8e3a4e 60%)"></i></div>
<svg class="carousel-arrow" style="left:1141px" width="14" height="24" viewBox="0 0 14 24"><path d="M2 2l10 10L2 22" fill="none" stroke="#999" stroke-width="1.5"/></svg>

<div class="btn-view">View All Products <svg width="8" height="10" viewBox="0 0 8 10"><path d="M2 1l4 4-4 4" fill="none" stroke="currentColor" stroke-width="2"/></svg></div>

<section class="testimonials">
  <h2 class="section-title" style="top:44px;font-size:31px">What People Are Saying</h2>
  <div class="review" style="left:-208px">
    <div class="stars">★★★★★</div>
    <p>Your Invitation quality are so-so good. I recommand to all new marriage, all guest liked<br>what you have done. Thanks for creating something beautifull for my special day thanks<br>again.</p>
    <div class="avatar"></div><b>Mariel T.</b>
  </div>
  <div class="review" style="left:341px">
    <div class="stars">★★★★★</div>
    <p>Your Invitation quality are so-so good. I recommand to all new marriage, all guest liked<br>what you have done. Thanks for creating something beautifull for my special day thanks<br>again.</p>
    <div class="avatar"></div><b>Dorian P.</b>
  </div>
  <div class="review" style="left:890px">
    <div class="stars">★★★★★</div>
    <p>Your Invitation quality are so-so good. I recommand to all new marriage, all guest liked<br>what you have done. Thanks for creating something beautifull for my special day thanks<br>again.</p>
    <div class="avatar"></div><b>Dorian P.</b>
  </div>
  <div class="pager"><i></i><i></i><i></i></div>
  <div class="abs" style="left:599px;top:464px;height:60px;border-left:1px solid #bbb"></div>
</section>

<section class="newsletter">
  <small>Sign up for our weeky deals and offers</small>
  <h2>Newsletter</h2>
  <div class="signup">
    <span><svg width="22" height="16" viewBox="0 0 22 16"><rect width="22" height="16" fill="#e0c6bb"/><path d="M1 1l10 8 10-8" fill="none" stroke="#5e1718" stroke-width="1.5"/></svg>Type your email address</span>
    <b>Sign up</b>
  </div>
</section>

<div class="social" style="left:0;width:250px;background:linear-gradient(135deg,#d9d9d6,#c8272d 40%,#e2e2df)" role="img" aria-label="Red laser cut church invitation with greenery"></div>
<div class="social" style="left:250px;width:244px;background:linear-gradient(135deg,#eceae8,#4aa595 45%,#efd6dd)" role="img" aria-label="Teal laser cut invitation beside pink roses"></div>
<div class="social follow" style="left:494px;width:210px">FOLLOW US<br>ON<br>PICTORA</div>
<div class="social" style="left:704px;width:245px;background:linear-gradient(135deg,#80411f,#f1ede6 45%,#e5d9c2 70%,#7a3b1d)" role="img" aria-label="Ivory laser cut invitation with white envelope on wood"></div>
<div class="social" style="left:949px;width:251px;background:linear-gradient(135deg,#6e361c,#c9a06a 50%,#8a4722)" role="img" aria-label="Gold butterfly laser cut invitation on wood"></div>

<div class="foot-col caps" style="left:177px">Home<br>About us<br>Products<br>News<br>Contact us</div>
<div class="foot-col caps" style="left:423px">Sitemap<br>Send inqueries<br>Shipping &amp; returns</div>
<div class="foot-col" style="left:668px;line-height:23px">Wedding invitation card<br>Laser cut favor box<br>Wedding stationary<br>Wedding decoration accessory<br>3D pop up card<br>Greeting card</div>
<div class="foot-col foot-social" style="left:911px">
  <small>BE PART OF OUR FAMILY</small>
  <strong>FOLLOW US</strong>
  <div class="icons"><i></i><i></i><i></i></div>
</div>

<div class="divider"></div>
<div class="foot-logo">Lovmira</div>
<div class="copyright">Lorem ipsum dolor sit amet, consectetur adipiscing elit. Nec nullam nullam nascetur tellus sed augue in enim.</div>

</div>
</body>
</html>
```